Business Card Design Project

Looking for a simple and stylish business card. We are an Advertising Company. The card Must feature the company logo (attached) and also this info.
p: 0481629054
e: sales@rv-promo.com.au
w: www.rv-promo.com.au
We Advertise mainly using TV screens featured in restaurants and cafe. See website for more about the business.
Not really looking for a plain background, but at the same time do not want to much happening in the Background. I am not really to fussy though with the design or the colour scheme, and I am leaving the creativity part up to you creative designers.

```html
<!DOCTYPE html>
<html lang="en">
<head>
<meta charset="utf-8">
<title>RV Promo Business Card</title>
<link rel="stylesheet" href="https://fonts.googleapis.com/css2?family=Mulish:wght@300;800&display=swap">
<style>
  :root {
    --page: #ffffff;
    --sky: #00ccff;
    --sun-top: #ffff00;
    --sun-bottom: #c2f23c;
    --magenta: #e8137a;
    --violet: #7d63b8;
    --coral: #de7658;
    --amber: #d8a84e;
    --olive: #b4a86a;
    --ink: #3a3a3a;
    --brand: #e8146f;
  }
  * { margin: 0; padding: 0; box-sizing: border-box; }
  html, body {
    width: 1200px;
    height: 1000px;
    overflow: hidden;
    background: var(--page);
  }
  .card {
    position: absolute;
    left: 191px;
    top: 266px;
    width: 817px;
    height: 467px;
    font-family: "Mulish", "Century Gothic", sans-serif;
  }
  .block { position: absolute; }
  .block--sky {
    left: 0; top: 0; width: 520px; height: 326px;
    background: var(--sky);
  }
  .block--sun {
    left: 520px; top: 0; width: 297px; height: 326px;
    background: linear-gradient(to bottom, var(--sun-top) 0%, var(--sun-top) 10%, var(--sun-bottom) 100%);
  }
  .block--contact {
    left: 0; top: 326px; width: 520px; height: 141px;
    background: linear-gradient(to right, var(--magenta) 5%, var(--violet) 100%);
  }
  .block--labels {
    left: 520px; top: 326px; width: 297px; height: 141px;
    background: linear-gradient(160deg, var(--coral) 0%, var(--amber) 55%, var(--olive) 100%);
  }
  .brand-name {
    position: absolute;
    right: 10px;
    top: 18px;
    font-weight: 300;
    font-size: 58px;
    line-height: 1;
    letter-spacing: 1px;
    color: var(--brand);
    white-space: nowrap;
  }
  .contact-list, .label-list {
    position: absolute;
    top: 337px;
    list-style: none;
    font-weight: 800;
    font-size: 25px;
    line-height: 43px;
    color: var(--ink);
  }
  .contact-list { right: 345px; text-align: right; }
  .label-list { left: 546px; text-align: left; }
</style>
</head>
<body>
  <div class="card">
    <div class="block block--sky"></div>
    <div class="block block--sun"></div>
    <div class="block block--contact"></div>
    <div class="block block--labels"></div>

    <div class="brand-name">RV PROMO</div>

    <ul class="contact-list">
      <li>0481629054</li>
      <li>sales@rv-promo.com.au</li>
      <li>www.rv-promo.com.au</li>
    </ul>
    <ul class="label-list">
      <li>phone</li>
      <li>email</li>
      <li>website</li>
    </ul>
  </div>
</body>
</html>
```